Wedding invitation - including print files

Details
45 invitations and envelopes required

Our names: Corin and Maribel

Wedding information
Venue
At the Thistlewood residence, 2847 Ferndale-Tarawhiti road, Clevedon, Auckland for both the ceremony and reception.

Date
Saturday 19th April 2025 (Easter weekend)

Timing
Ceremony is at 3pm

Transport
A bus will pick up at 1.30pm from Harbour Lantern Hotel
A bus will go back to town to at 11pm and 12.15am to Harbour Lantern Hotel with a stop through Clevedon for those staying closer to the venue.

Accomodation
A lot of airbnbs and hotels in clevedon if you wish to stay closer

Gifts
gifts aren’t necessary but a wishing well for a piece of art we will remember the day by.

Day After
We will be having some platters from 1pm on Sunday at (I will confirm this to you tomorrow sorry we are choosing between two places)

RSVP
By the 12th October 2024 to Corin 0274918265 corin@brookfieldgroup.co or Maribel 0275306194 maribel@lumastudio.co.nz

Here are concept ideas for the invitations and the aspects we like about them.
Three sided is practical to fit information

Font styles to use
Decorative

Colors

Designer to choose only greyscale colors for use in the design.

Requirements
Nice to have
• refer attachments and description
Should not have
• cant look cheap or tacky

```html
<!DOCTYPE html>
<html lang="en">
<head>
<meta charset="utf-8">
<title>Maribel &amp; Corin – Wedding Invitation</title>
<link rel="stylesheet" href="https://fonts.googleapis.com/css2?family=Cormorant+Garamond:ital,wght@0,400;0,500;1,400&family=Great+Vibes&family=Playfair+Display:wght@700&display=swap">
<style>
  :root {
    --backdrop: #d4d4d4;
    --paper: #eeeeee;
    --fold: #ffffff;
    --ink: #3c3c3c;
    --ink-deep: #262626;
    --floral: #6e6e6e;
    --floral-strong: rgba(90,90,90,.5);
    --floral-mid: rgba(90,90,90,.22);
    --floral-soft: rgba(90,90,90,0);
  }
  * { margin: 0; padding: 0; box-sizing: border-box; }
  html, body { width: 799px; height: 1200px; overflow: hidden; }
  body {
    position: relative;
    background: var(--backdrop);
    font-family: "Cormorant Garamond", Georgia, serif;
    color: var(--ink);
  }
  .card { position: absolute; background: var(--paper); overflow: hidden; }
  .cover { left: 214px; top: 43px; width: 379px; height: 531px; }
  .inside { left: 20px; top: 634px; width: 759px; height: 530px; }
  .fold-line { position: absolute; top: 0; bottom: 0; width: 1px; background: var(--fold); }
  .floral { position: absolute; }
  .cover .floral-top {
    left: 0; top: 0; width: 217px; height: 146px;
    background: radial-gradient(ellipse at 20% 15%, var(--floral-strong), var(--floral-mid) 55%, var(--floral-soft) 72%);
  }
  .cover .floral-bottom {
    right: 0; bottom: 0; width: 224px; height: 151px;
    background: radial-gradient(ellipse at 80% 85%, var(--floral-strong), var(--floral-mid) 55%, var(--floral-soft) 72%);
  }
  .monogram { position: absolute; left: 0; top: 0; width: 379px; height: 531px; }
  .monogram-frame { position: absolute; left: 111px; top: 185px; }
  .monogram-floral {
    left: 132px; top: 206px; width: 122px; height: 130px; border-radius: 50%;
    background: radial-gradient(ellipse at center, var(--floral-strong), var(--floral-mid) 60%, var(--floral-soft) 75%);
  }
  .initial {
    position: absolute;
    font-family: "Playfair Display", Georgia, serif;
    font-weight: 700; font-size: 54px; line-height: 1;
    color: var(--ink-deep);
  }
  .initial-first { left: 124px; top: 198px; }
  .initial-second { left: 214px; top: 278px; }

  .inside .floral-top {
    left: 0; top: 0; width: 225px; height: 151px;
    background: radial-gradient(ellipse at 25% 20%, var(--floral-strong), var(--floral-mid) 55%, var(--floral-soft) 72%);
  }
  .inside .floral-bottom {
    right: 0; bottom: 0; width: 218px; height: 146px;
    background: radial-gradient(ellipse at 78% 80%, var(--floral-strong), var(--floral-mid) 55%, var(--floral-soft) 72%);
  }
  .crest { position: absolute; left: 360px; top: 31px; }
  .crest-sprig {
    left: 370px; top: 44px; width: 20px; height: 46px; border-radius: 50%;
    background: linear-gradient(var(--floral-strong), var(--floral-mid));
  }

  .text-block { position: absolute; text-align: center; white-space: nowrap; }
  .caps { text-transform: uppercase; letter-spacing: .06em; }
  .italic { font-style: italic; }

  .main { left: 190px; width: 380px; }
  .line { display: block; }
  .lead { font-size: 11.5px; }
  .lead-italic { font-size: 12.5px; }
  .name { font-size: 26px; letter-spacing: .07em; line-height: 1; font-weight: 400; text-transform: uppercase; }
  .and { font-family: "Great Vibes", cursive; font-size: 20px; line-height: 1; }
  .detail-italic { font-size: 14px; }
  .detail-caps { font-size: 12.5px; }

  .side-left { left: 0; width: 190px; }
  .side-right { left: 570px; width: 189px; }
  .info-heading { font-size: 10px; letter-spacing: .04em; text-transform: uppercase; display: block; line-height: 14px; margin-bottom: 2px; }
  .info-body { font-size: 9.6px; font-style: italic; line-height: 12.3px; display: block; }
</style>
</head>
<body>

<section class="card cover" aria-label="Invitation cover">
  <div class="floral floral-top" role="img" aria-label="Grey line-drawn floral corner of hibiscus and leaves"></div>
  <div class="floral floral-bottom" role="img" aria-label="Grey line-drawn floral corner of roses, hibiscus and leaves"></div>
  <div class="fold-line" style="left:189px"></div>

  <div class="monogram">
    <svg class="monogram-frame" width="156" height="156" viewBox="0 0 156 156" aria-hidden="true">
      <rect x="28" y="28" width="100" height="100" rx="12" transform="rotate(45 78 78)" fill="none" stroke="var(--floral)" stroke-width="0.8"/>
    </svg>
    <div class="floral monogram-floral" role="img" aria-label="Grey floral bouquet within the monogram frame"></div>
    <span class="initial initial-first">M</span>
    <span class="initial initial-second">C</span>
  </div>
</section>

<section class="card inside" aria-label="Invitation inside">
  <div class="floral floral-top" role="img" aria-label="Grey line-drawn floral corner of hibiscus, roses and leaves"></div>
  <div class="floral floral-bottom" role="img" aria-label="Grey line-drawn floral corner of hibiscus and leaves"></div>
  <div class="fold-line" style="left:190px"></div>
  <div class="fold-line" style="left:570px"></div>

  <svg class="crest" width="40" height="72" viewBox="0 0 40 72" aria-hidden="true">
    <rect x="0.5" y="0.5" width="39" height="71" rx="19.5" fill="none" stroke="var(--floral)" stroke-width="0.8"/>
    <rect x="3" y="3" width="34" height="66" rx="17" fill="none" stroke="var(--floral)" stroke-width="0.6"/>
  </svg>
  <div class="floral crest-sprig" role="img" aria-label="Small floral sprig"></div>

  <div class="text-block main" style="top:117px">
    <span class="line caps lead" style="line-height:17px">It is with great joy</span>
    <span class="line italic lead-italic" style="line-height:20px">that together</span>
    <span class="line caps lead" style="line-height:22px">with their families</span>
  </div>

  <div class="text-block main" style="top:199px">
    <h1 class="line name">Maribel</h1>
    <span class="line and" style="margin-top:10px">and</span>
    <h2 class="line name" style="margin-top:12px">Corin</h2>
  </div>

  <div class="text-block main" style="top:328px">
    <span class="line italic detail-italic" style="line-height:20px">invite you to the celebration of their wedding</span>
    <span class="line caps detail-caps" style="line-height:20px">On Saturday, the nineteenth of April</span>
    <span class="line italic detail-italic" style="line-height:22px">two thousand twenty-five</span>
    <span class="line caps detail-caps" style="line-height:20px; margin-top:15px">At 3 o’clock in the afternoon</span>
    <span class="line italic detail-italic" style="line-height:17px; margin-top:20px">At the Thistlewood residence, 2847 Ferndale-</span>
    <span class="line italic detail-italic" style="line-height:17px">Tarawhiti road, Clevedon, Auckland for both</span>
    <span class="line italic detail-italic" style="line-height:17px">the ceremony and reception</span>
  </div>

  <div class="text-block side-left" style="top:202px">
    <span class="info-heading">Accomodation</span>
    <span class="info-body">A lot of airbnbs and hotels in<br>clevedon if you wish to stay closer</span>
  </div>
  <div class="text-block side-left" style="top:293px">
    <span class="info-heading">Gifts</span>
    <span class="info-body">gifts aren’t necessary but a wishing<br>well for a piece of art we will<br>remember the day by.</span>
  </div>
  <div class="text-block side-left" style="top:396px">
    <span class="info-heading">Day after</span>
    <span class="info-body">We will be having some platters from<br>1pm on Sunday at ...</span>
  </div>

  <div class="text-block side-right" style="top:56px">
    <span class="info-heading">Transport</span>
    <span class="info-body">A bus will pick up at 1.30pm from<br>Harbour Lantern Hotel<br>~<br>A bus will go back to town to at<br>11pm and 12.15am to Harbour<br>Lantern Hotel<br>with a stop through Clevedon for<br>those staying closer to the venue</span>
  </div>
  <div class="text-block side-right" style="top:234px">
    <span class="info-heading">RSVP</span>
    <span class="info-body">By the 12th October 2024 to<br>Corin 0274918265<br>corin@brookfieldgroup.co<br>or<br>Maribel 0275306194<br>maribel@lumastudio.co.nz</span>
  </div>
</section>

</body>
</html>
```